Property development company needs a name card design

I started my company since 2010, based in Auckland, New Zealand. We have been doing residential property rentals, individual low-rise residential property construction, small to medium scale residential development project. We will be participate in property investment as well. I have no favor of any specific design or color, just be creative and do anything you think will match the concept.

```html
<!DOCTYPE html>
<html lang="en">
<head>
<meta charset="UTF-8">
<title>Kowhai investment &amp; development Ltd – Business Card</title>
<link href="https://fonts.googleapis.com/css2?family=Barlow:wght@400;600;700&display=swap" rel="stylesheet">
<style>
  :root {
    --sky: #4fc8f2;
    --paper: #ffffff;
  }
  * { margin: 0; padding: 0; box-sizing: border-box; }
  html, body {
    width: 1200px;
    height: 685px;
    overflow: hidden;
    background: var(--paper);
  }
  .card {
    position: relative;
    width: 1200px;
    height: 685px;
    background: var(--paper);
    font-family: "Barlow", "DIN Alternate", Arial, sans-serif;
  }
  .card__header {
    position: absolute;
    top: 0; left: 0;
    width: 100%;
    height: 120px;
    display: flex;
    align-items: center;
    padding-left: 64px;
  }
  .company-name {
    color: var(--sky);
    font-size: 50px;
    font-weight: 400;
    letter-spacing: 0.5px;
    line-height: 1;
    padding-bottom: 4px;
  }
  .card__body {
    position: absolute;
    top: 120px; left: 0;
    width: 100%;
    height: 565px;
    background: var(--sky);
  }
  .brand-mark {
    position: absolute;
    left: 45px;
    top: 134px;
    width: 372px;
    height: 372px;
  }
  .holder {
    position: absolute;
    right: 50px;
    top: 150px;
    text-align: right;
    color: var(--paper);
  }
  .holder__name {
    font-size: 86px;
    font-weight: 700;
    line-height: 1;
    letter-spacing: 2px;
  }
  .holder__title {
    margin-top: 20px;
    font-size: 49px;
    font-weight: 700;
    line-height: 1;
    letter-spacing: 1.5px;
  }
  .contact {
    position: absolute;
    right: 50px;
    top: 396px;
    list-style: none;
    text-align: right;
    color: var(--paper);
    font-size: 33px;
    font-weight: 600;
    line-height: 45px;
  }
</style>
</head>
<body>
  <div class="card">
    <header class="card__header">
      <h1 class="company-name">Kowhai investment &amp; development Ltd</h1>
    </header>
    <section class="card__body">
      <svg class="brand-mark" viewBox="0 0 372 372" aria-hidden="true">
        <circle cx="186" cy="186" r="170" fill="none" stroke="#ffffff" stroke-width="16"/>
      </svg>
      <div class="holder">
        <p class="holder__name">GRACE CHEN</p>
        <p class="holder__title">DIRECTOR</p>
      </div>
      <ul class="contact">
        <li class="contact__phone">021.555.0194</li>
        <li class="contact__email">grace.chen@kowhaidev.com</li>
        <li class="contact__web">www.kowhaidev.com</li>
      </ul>
    </section>
  </div>
</body>
</html>
```